New Email Marketing Design Project

I’d like you to make an email template. I’ll be welcoming and on boarding customers via email. And I’d like the branding to stand out. Keep it professional and simple. But be creative.

Design should look amazing on desktop and mobile phones.

Negative white space is ok.

Use stock images

I’ll like to have a spot for a picture of myself so make sure to include a circle where I can show my face so that email viewers will know who is speaking to them.

Target Market(s)

Practice managers, doctors, medical providers

Font styles to use
Sans Serif

Requirements
Must have
• Our Logo, CTA buttons, Same colors as website.
https://www.tavrenhealthclaims.com

```html
<!DOCTYPE html>
<html lang="en">
<head>
<meta charset="utf-8">
<title>Tavren Health Claims — Welcome</title>
<link href="https://fonts.googleapis.com/css2?family=Lato:wght@400;700;900&display=swap" rel="stylesheet">
<style>
  :root{
    --brand:#2b6a93;
    --brand-dark:#245a7e;
    --ink:#141414;
    --text:#2a2a2a;
    --muted-bg:#efefef;
    --dark-bg:#111111;
    --footer-bg:#232323;
    --white:#ffffff;
  }
  *{box-sizing:border-box;margin:0;padding:0}
  html,body{width:1200px;height:4500px;overflow:hidden;background:var(--white)}
  body{font-family:'Lato',sans-serif;color:var(--text);position:relative}
  .section{position:absolute;left:0;width:1200px}
  .btn{position:absolute;display:flex;align-items:center;justify-content:center;width:256px;height:79px;background:var(--brand);color:var(--white);font-weight:700;font-size:28px;text-transform:uppercase;text-decoration:none;border-radius:2px}
  .btn--dark{background:var(--ink)}
  .heading{position:absolute;left:0;width:100%;text-align:center;font-weight:900;font-size:56px;color:var(--ink);text-transform:uppercase;letter-spacing:-0.5px}
  .copy{position:absolute;text-align:center;font-size:24px;line-height:44px;color:var(--text)}

  /* header */
  .topbar{top:0;height:128px;background:var(--white)}
  .brand{position:absolute;left:40px;top:36px;display:flex;align-items:center;gap:16px}
  .brand__dot{width:56px;height:56px;border-radius:50%;background:var(--brand)}
  .brand__name{font-weight:900;font-size:30px;color:var(--brand)}
  .helpline{position:absolute;left:513px;top:28px;display:flex;gap:14px;align-items:center}
  .helpline__label{font-size:28px;font-weight:700;color:var(--ink);line-height:34px}
  .helpline__number{font-size:34px;font-weight:900;color:var(--brand);line-height:40px}
  .topbar .btn{left:907px;top:26px;width:257px}

  /* hero */
  .hero{top:128px;height:635px;background:linear-gradient(120deg,#e9e6ea 0%,#f3eeee 35%,#e6d3d0 55%,#c9b1ab 70%,#6b6f74 100%)}
  .hero__title{top:180px;font-size:57px}
  .hero__sub{left:40px;width:1120px;top:250px;font-size:27px;line-height:42px;color:#1c1c1c}
  .hero .btn{left:472px;top:366px}

  /* about */
  .about{top:763px;height:591px}
  .about .heading{top:62px}
  .about .copy{left:96px;width:1008px;top:146px}
  .about .btn{left:472px;top:411px}

  /* services */
  .services{top:1354px;height:1050px;background:var(--muted-bg)}
  .services .heading{top:76px}
  .service-card{position:absolute;width:353px;height:301px;background:var(--white);text-align:center}
  .service-card svg{position:absolute;left:130px;top:50px}
  .service-card__label{position:absolute;left:0;top:185px;width:100%;font-size:24px;font-weight:700;line-height:36px;text-transform:uppercase;color:#222}
  .services .btn{top:893px}

  /* about me */
  .about-me{top:2404px;height:508px;background:var(--dark-bg)}
  .portrait{position:absolute;left:63px;top:77px;width:356px;height:356px;border-radius:50%;background:radial-gradient(circle at 50% 40%,#d9d4cf 0%,#a49c95 45%,#3c3f46 100%)}
  .about-me__title{position:absolute;left:473px;top:62px;font-size:56px;font-weight:900;color:var(--white);text-transform:uppercase}
  .about-me__copy{position:absolute;left:473px;top:145px;width:640px;font-size:24px;line-height:44px;color:#e8e8e8}
  .about-me .btn{left:473px;top:355px}

  /* revenue cycle */
  .revenue{top:2912px;height:687px}
  .revenue .heading{top:66px}
  .revenue__photo{position:absolute;left:35px;top:191px;width:543px;height:424px;background:linear-gradient(90deg,#8f8f8f 0%,#d8d5d0 30%,#f1efec 60%,#5a6068 100%)}
  .checklist{position:absolute;left:613px;top:200px;width:540px;list-style:none}
  .checklist li{position:relative;padding-left:55px;font-size:23px;line-height:37px;margin-bottom:6px;color:#333}
  .checklist svg{position:absolute;left:0;top:8px}
  .revenue .btn{left:613px;top:535px}

  /* call to action */
  .cta{top:3599px;height:500px;background:var(--brand)}
  .cta .heading{top:70px;color:var(--white)}
  .cta .copy{left:105px;width:990px;top:145px;color:#e6eef4}
  .cta .btn{left:473px;top:342px}

  /* contact */
  .contact{top:4099px;height:230px}
  .contact__row{position:absolute;left:0;width:100%;display:flex;justify-content:center;align-items:center;gap:48px;color:var(--ink)}
  .contact__phone{top:42px;font-size:62px;font-weight:400}
  .contact__email{top:132px;font-size:40px}

  /* footer */
  .footer{top:4329px;height:171px;background:var(--footer-bg);color:#dcdcdc}
  .footer__copyright{position:absolute;left:37px;top:78px;font-size:20px}
  .social{position:absolute;right:34px;top:70px;display:flex;gap:32px}
  .social__item{display:block;width:36px;height:36px;border-radius:4px;background:var(--white)}
</style>
</head>
<body>

<header class="section topbar">
  <div class="brand"><span class="brand__dot"></span><span class="brand__name">Tavren Health Claims</span></div>
  <div class="helpline">
    <svg width="36" height="62" viewBox="0 0 36 62"><rect x="3" y="3" width="30" height="56" rx="6" fill="none" stroke="var(--brand-dark)" stroke-width="5"/><rect x="8" y="11" width="20" height="36" fill="var(--brand-dark)"/><circle cx="18" cy="53" r="2.5" fill="var(--brand-dark)"/></svg>
    <div><div class="helpline__label">Need Help? Call Us Now</div><div class="helpline__number">16125550187</div></div>
  </div>
  <a class="btn" href="https://www.tavrenhealthclaims.com">Get in touch</a>
</header>

<section class="section hero" role="img" aria-label="Photo of a hand using a calculator beside a laptop keyboard and paperwork">
  <h1 class="heading hero__title">Tavren Health Claims</h1>
  <p class="copy hero__sub">Tavren Health Claims will allow you to save on overhead expenses such as salaries, payroll taxes, benefits, and printing/office supplies.</p>
  <a class="btn" href="https://www.tavrenhealthclaims.com">Get in touch</a>
</section>

<section class="section about">
  <h2 class="heading">About Us</h2>
  <p class="copy">At Tavren Health Claims we are focused on providing medical billing services with the highest levels of customer satisfaction &amp; we will do everything we can to meet your expectations. With a variety of offerings to choose from, we’re sure you’ll be happy working with us. Tavren Health Claims is a company that you can place your trust in.<br>We offer comprehensive and secure billing support.</p>
  <a class="btn" href="https://www.tavrenhealthclaims.com">Get in touch</a>
</section>

<section class="section services">
  <h2 class="heading">Our Services</h2>

  <div class="service-card" style="left:35px;top:185px">
    <svg width="94" height="94" viewBox="0 0 94 94" fill="none" stroke="var(--brand)" stroke-width="3"><circle cx="38" cy="38" r="30"/><circle cx="38" cy="38" r="22"/><path d="M60 60l26 26"/><path d="M20 40h8l5-10 6 18 5-8h12"/></svg>
    <div class="service-card__label">Insurance<br>Eligibility Check</div>
  </div>
  <div class="service-card" style="left:424px;top:185px">
    <svg width="94" height="94" viewBox="0 0 94 94" fill="none" stroke="var(--brand)" stroke-width="3"><rect x="32" y="10" width="56" height="60" rx="3"/><path d="M42 24h36M42 36h36M42 48h26"/><circle cx="20" cy="40" r="10"/><path d="M4 86c0-16 8-26 16-26s16 10 16 26z"/></svg>
    <div class="service-card__label">Clearinghouse<br>Maintenance</div>
  </div>
  <div class="service-card" style="left:812px;top:185px">
    <svg width="94" height="94" viewBox="0 0 94 94" fill="none" stroke="var(--brand)" stroke-width="3"><path d="M10 6h40l14 14v68H10z"/><path d="M24 36l13-6 13 6v12c0 8-6 14-13 18-7-4-13-10-13-18z"/><path d="M31 46l5 5 8-9"/><circle cx="72" cy="54" r="9"/><path d="M56 88c0-14 7-22 16-22s16 8 16 22z"/></svg>
    <div class="service-card__label">Insurance<br>Credentialing</div>
  </div>
  <div class="service-card" style="left:35px;top:524px">
    <svg width="94" height="94" viewBox="0 0 94 94" fill="none" stroke="var(--brand)" stroke-width="3"><path d="M14 6h52v82H14z"/><path d="M24 20h32M24 32h32M24 44h20M24 56h16M24 68h16"/><circle cx="66" cy="58" r="18"/><path d="M66 48v20M56 58h20"/></svg>
    <div class="service-card__label">Medical<br>Billing</div>
  </div>
  <div class="service-card" style="left:424px;top:524px">
    <svg width="94" height="94" viewBox="0 0 94 94" fill="none" stroke="var(--brand)" stroke-width="3"><circle cx="22" cy="22" r="14"/><path d="M22 36l-6 14h12z"/><ellipse cx="52" cy="62" rx="18" ry="6"/><path d="M34 62v18c0 3 8 6 18 6s18-3 18-6V62"/><circle cx="74" cy="70" r="12"/><path d="M50 40l12-14 10 8 14-20M78 14h8v8"/></svg>
    <div class="service-card__label">Revenue Cycle<br>Analysis</div>
  </div>
  <div class="service-card" style="left:812px;top:524px">
    <svg width="94" height="94" viewBox="0 0 94 94" fill="none" stroke="var(--brand)" stroke-width="3"><rect x="8" y="6" width="58" height="82"/><rect x="16" y="14" width="42" height="18"/><path d="M20 42h6v6h-6zM20 56h6v6h-6zM20 70h6v6h-6zM32 45h24M32 59h20"/><circle cx="70" cy="66" r="16"/><path d="M62 74l16-16"/><circle cx="64" cy="60" r="2.5"/><circle cx="76" cy="72" r="2.5"/></svg>
    <div class="service-card__label">Claim<br>Appeals</div>
  </div>

  <a class="btn" style="left:332px" href="https://www.tavrenhealthclaims.com">Read more</a>
  <a class="btn btn--dark" style="left:613px" href="https://www.tavrenhealthclaims.com">Get in touch</a>
</section>

<section class="section about-me">
  <div class="portrait" role="img" aria-label="Circular portrait photo of the sender"></div>
  <h2 class="about-me__title">About Me</h2>
  <p class="about-me__copy">At Tavren Health Claims we are focused on providing medical billing services with the highest levels of customer satisfaction &amp; we will do everything we can to meet your expectations.</p>
  <a class="btn" href="https://www.tavrenhealthclaims.com">Get in touch</a>
</section>

<section class="section revenue">
  <h2 class="heading">Revenue Cycle Management</h2>
  <div class="revenue__photo" role="img" aria-label="Stock photo of colleagues reviewing financial charts at a desk"></div>
  <ul class="checklist">
    <li><svg width="22" height="22" viewBox="0 0 22 22"><circle cx="11" cy="11" r="11" fill="var(--brand)"/><path d="M6 11l4 4 6-8" fill="none" stroke="#fff" stroke-width="2.5"/></svg>Low level of collections and large accounts receivable backlogs</li>
    <li><svg width="22" height="22" viewBox="0 0 22 22"><circle cx="11" cy="11" r="11" fill="var(--brand)"/><path d="M6 11l4 4 6-8" fill="none" stroke="#fff" stroke-width="2.5"/></svg>Retention and management of billing staff</li>
    <li><svg width="22" height="22" viewBox="0 0 22 22"><circle cx="11" cy="11" r="11" fill="var(--brand)"/><path d="M6 11l4 4 6-8" fill="none" stroke="#fff" stroke-width="2.5"/></svg>Rising costs of administration and processing services</li>
    <li><svg width="22" height="22" viewBox="0 0 22 22"><circle cx="11" cy="11" r="11" fill="var(--brand)"/><path d="M6 11l4 4 6-8" fill="none" stroke="#fff" stroke-width="2.5"/></svg>Lack of qualified personnel and billing resources</li>
    <li><svg width="22" height="22" viewBox="0 0 22 22"><circle cx="11" cy="11" r="11" fill="var(--brand)"/><path d="M6 11l4 4 6-8" fill="none" stroke="#fff" stroke-width="2.5"/></svg>Increasing need for IT capital expenditures</li>
  </ul>
  <a class="btn" href="https://www.tavrenhealthclaims.com">Read more</a>
</section>

<section class="section cta">
  <h2 class="heading">Ready to get started?</h2>
  <p class="copy">Tavren Health Claims is a company that you can place your trust in. We offer comprehensive and secure billing support and ensure that your claims will sail through the processing stage. The company is HIPPA compliant and cares about the security of your medical data as much as you do.</p>
  <a class="btn btn--dark" href="https://www.tavrenhealthclaims.com">Contact us</a>
</section>

<section class="section contact">
  <div class="contact__row contact__phone">
    <svg width="48" height="48" viewBox="0 0 24 24"><path fill="var(--brand)" d="M6.6 10.8a15.1 15.1 0 006.6 6.6l2.2-2.2c.3-.3.7-.4 1-.2 1.1.4 2.3.6 3.6.6.6 0 1 .4 1 1V20c0 .6-.4 1-1 1A17 17 0 013 4c0-.6.4-1 1-1h3.5c.6 0 1 .4 1 1 0 1.3.2 2.5.6 3.6.1.3 0 .7-.2 1z"/></svg>
    <span>612-555-0187</span>
  </div>
  <div class="contact__row contact__email">
    <svg width="48" height="36" viewBox="0 0 48 36"><rect width="48" height="36" rx="3" fill="var(--brand)"/><path d="M3 4l21 16L45 4" fill="none" stroke="#fff" stroke-width="3"/></svg>
    <span>hello@tavrenhealthclaims.com</span>
  </div>
</section>

<footer class="section footer">
  <p class="footer__copyright">Copyright © 2020. Company Name.&nbsp; All Right Reserved</p>
  <nav class="social" aria-label="Social links">
    <span class="social__item"></span>
    <span class="social__item"></span>
    <span class="social__item"></span>
    <span class="social__item"></span>
    <span class="social__item"></span>
  </nav>
</footer>

</body>
</html>
```